Brochure for medical doctor

I need a brochure for a medical doctor to promote his practice. The brochure should contain his picture, business information (use letterhead from attachment), and the following text:

- Now accepting PI cases on lien!
- Same and next business day appointments available for initial visits, pre-operative clearances, and all other medical needs

- Expedited medical reports sent quickly to your office

Medical

```html
<!DOCTYPE html>
<html lang="en">
<head>
<meta charset="utf-8">
<title>Willow Park Medical Center – Flyer</title>
<link href="https://fonts.googleapis.com/css2?family=Oswald:wght@300;400;500;600&family=Open+Sans:wght@400;600;700&display=swap" rel="stylesheet">
<style>
  :root{
    --red:#d71f26;
    --ink:#1f1f1f;
    --grey-text:#6b6b6b;
    --band:#3d3d40;
    --paper:#ffffff;
    --backdrop:#e4e4e4;
    --photo-light:#e9e6e2;
    --photo-mid:#cfc8c0;
  }
  *{margin:0;padding:0;box-sizing:border-box}
  html,body{width:1200px;height:772px;overflow:hidden;background:var(--backdrop)}
  .flyer{
    position:absolute;left:314px;top:16px;width:572px;height:740px;
    background:var(--paper);overflow:hidden;
    font-family:"Open Sans",sans-serif;color:var(--ink);
    box-shadow:0 2px 10px rgba(0,0,0,.15);
  }
  .art{position:absolute;left:0;top:0;width:572px;height:470px}
  .brand{position:absolute;left:26px;top:34px;display:flex;align-items:center;gap:8px}
  .brand-mark{width:20px;height:20px;background:var(--red)}
  .brand-name{font-family:"Oswald",sans-serif;font-weight:600;font-size:20px;color:var(--red);letter-spacing:.3px;line-height:1.05}
  .headline{position:absolute;left:18px;top:176px;font-family:"Oswald",sans-serif;font-weight:500;line-height:1.22}
  .headline .lead{display:block;color:var(--red);font-size:29px;letter-spacing:-.4px}
  .headline .main{display:block;color:var(--ink);font-size:29px;letter-spacing:-.6px}
  .lien-photo,.portrait{position:absolute;border-radius:50%}
  .lien-photo{left:146px;top:281px;width:168px;height:168px;
    background:linear-gradient(160deg,#3a3a3a 0 18%,#f4f4f4 19%,#e2e2e2 100%);
    border:2px solid #fff;box-shadow:0 2px 6px rgba(0,0,0,.25)}
  .intro{position:absolute;left:0;width:572px;top:487px;text-align:center;font-size:17px;line-height:22px;color:var(--ink)}
  .pill{position:absolute;left:41px;top:547px;width:483px;height:34px;border-radius:17px;background:var(--red);
    color:#fff;font-weight:700;font-size:14px;letter-spacing:.2px;display:flex;align-items:center;justify-content:center;
    box-shadow:0 2px 4px rgba(0,0,0,.2)}
  .address{position:absolute;left:0;width:572px;top:586px;text-align:center;font-size:14px;color:var(--ink)}
  .hours{position:absolute;left:0;width:572px;top:613px;text-align:center;font-size:11px;color:var(--grey-text)}
  .footer-band{position:absolute;left:0;top:648px;width:572px;height:58px;background:var(--band)}
  .call-tab{position:absolute;left:353px;top:678px;width:219px;height:28px;background:var(--red);
    clip-path:polygon(16px 0,100% 0,100% 100%,0 100%)}
  .doctor{position:absolute;left:155px;top:654px;color:#fff}
  .doctor-name{font-family:"Oswald",sans-serif;font-weight:300;font-size:19px;line-height:1.2}
  .doctor-role{font-size:11px;font-weight:600;margin-top:2px}
  .appt{position:absolute;right:12px;top:660px;color:#fff;font-size:11px}
  .phone{position:absolute;right:12px;top:682px;color:#fff;font-weight:700;font-size:15px;letter-spacing:.3px}
  .portrait{left:14px;top:609px;width:124px;height:124px;border:4px solid #fff;
    background:linear-gradient(160deg,var(--photo-mid),#8a7a6a);box-shadow:0 1px 4px rgba(0,0,0,.3)}
  .web{position:absolute;left:0;width:572px;padding-left:120px;top:715px;text-align:center;font-size:12px;font-weight:600;letter-spacing:1px;color:var(--ink)}
  .web span{color:var(--red)}
</style>
</head>
<body>
  <main class="flyer">
    <svg class="art" viewBox="0 0 572 470">
      <defs>
        <linearGradient id="photoTone" x1="0" y1="0" x2="1" y2="1">
          <stop offset="0" stop-color="#f3f1ee"/>
          <stop offset=".6" stop-color="#e9e6e2"/>
          <stop offset="1" stop-color="#cfc8c0"/>
        </linearGradient>
        <radialGradient id="haloTone" cx=".45" cy=".4" r=".6">
          <stop offset="0" stop-color="#ffffff"/>
          <stop offset="1" stop-color="#e6e6e6"/>
        </radialGradient>
      </defs>
      <circle cx="108" cy="225" r="121" fill="url(#haloTone)"/>
      <path d="M322 0 C272 40 236 150 236 250 C236 380 370 450 572 430 L572 0 Z" fill="var(--red)"/>
      <path role="img" aria-label="Photo of a doctor in a white coat consulting with a patient"
            d="M338 0 C286 48 249 150 249 250 C249 365 380 430 572 412 L572 0 Z" fill="url(#photoTone)"/>
    </svg>

    <div class="brand">
      <span class="brand-mark"></span>
      <span class="brand-name">WILLOW PARK MEDICAL<br>CENTER</span>
    </div>

    <h1 class="headline">
      <span class="lead">NOW ACCEPTING</span>
      <span class="main">PI CASES ON LIEN!</span>
    </h1>

    <div class="lien-photo" role="img" aria-label="Photo of a claim of lien document with a pen"></div>

    <p class="intro">Same and next business day appointments available for initial visits,<br>pre-operative clearances, and all other medical needs</p>

    <div class="pill">EXPEDITED MEDICAL REPORTS SENT QUICKLY TO YOUR OFFICE</div>

    <p class="address">4610 Linden Ave. Maple Grove, CA 90512</p>
    <p class="hours">Mon-Fri : 9:00 am - 5:00 pm Saturday &amp; Sunday Closed</p>

    <div class="footer-band"></div>
    <div class="call-tab"></div>

    <div class="portrait" role="img" aria-label="Portrait photo of the physician"></div>

    <div class="doctor">
      <p class="doctor-name">Daniel Moreno, M.D.</p>
      <p class="doctor-role">Family Practice Physician</p>
    </div>
    <p class="appt">APPOINTMENT</p>
    <p class="phone">CALL US : (555) 014-2280</p>

    <p class="web">www.<span>WillowParkMedical</span>.com</p>
  </main>
</body>
</html>
```